International Trade Consulting Firm Seeks Quality Newsletter Design

Our company provides consulting services to Meridian 700 type companies. We compete with the largest consulting companies in the world. However, we have the highest level of expertise in the industry and need to look the most professional and high end. We have very relevant and important information to provide our customers about their compliance and projects. We will have the winning design coded to be an e-newsletter, so it needs to be one page. We want to keep our company colors and logo design in the newsletter, they are attached. We DO NOT want it to look like a mini-version of our website. We want a fresh look to this marketing piece. Newsletter will need to include title, possible sub-heading, space for a feature story, 2 other stories included, and space on either the left or right for short cuts, links or highlights of other articles. Contents/'In this issue' section, about us or branding area, section for relevant links, etc...
Target Market(s)
Meridian 700 companies, High-level management
Industry/Entity Type
Marketing

```html
<!DOCTYPE html>
<html lang="en">
<head>
<meta charset="utf-8">
<title>Harborline Trade Group Newsletter — May 2014</title>
<link href="https://fonts.googleapis.com/css2?family=Barlow:ital,wght@0,300;0,400;0,500;0,600;0,700;1,400;1,600;1,700&display=swap" rel="stylesheet">
<style>
  :root{
    --ink:#1a1a1a;
    --black:#000;
    --white:#fff;
    --green:#7ab648;
    --blue:#1ba1e2;
    --panel-blue:#eef6fc;
    --panel-cream:#fdfbec;
    --rule:#b9b9b9;
    --photo:#e6e7e8;
    --frame:#c5dcb0;
  }
  *{box-sizing:border-box;margin:0;padding:0}
  html,body{width:927px;height:1200px;overflow:hidden;background:var(--white)}
  body{position:relative;font-family:"Barlow",Arial,sans-serif;color:var(--ink)}

  .masthead{position:absolute;left:0;top:0;width:927px;height:130px;background:var(--black)}
  .brand{position:absolute;left:18px;top:22px;width:230px;color:var(--green);font-weight:700;font-size:24px;line-height:27px;text-transform:uppercase;letter-spacing:1px}
  .title{position:absolute;left:268px;top:4px;color:var(--white);font-weight:500;font-size:90px;letter-spacing:1px;line-height:96px;white-space:nowrap}
  .tagline{position:absolute;left:280px;top:94px;color:var(--white);font-style:italic;font-weight:600;font-size:14.5px}
  .issue{position:absolute;left:866px;top:80px;color:var(--white);font-weight:700;font-size:11px;line-height:14px}

  .sidebar-head{position:absolute;left:24px;width:212px;height:32px;background:var(--green);color:var(--white);font-weight:700;font-size:19px;letter-spacing:1px;text-align:center;line-height:32px;text-transform:uppercase}
  .sidebar-panel{position:absolute;left:24px;width:212px}
  .sidebar-rule{position:absolute;left:24px;width:212px;height:1px;background:var(--rule)}
  .about{top:177px;height:285px;background:var(--panel-blue);padding:16px 18px 0 22px;font-size:14.5px;line-height:20.5px}
  .contents{top:530px;height:352px;background:var(--panel-cream);padding:20px 0 0 16px;list-style:none}
  .contents li{position:relative;padding-left:20px;font-size:14.5px;line-height:22px;margin-bottom:24px}
  .contents li::before{content:"+";position:absolute;left:0;top:0;color:var(--green);font-weight:600}
  .links{top:948px;height:203px;background:var(--panel-blue);padding:14px 0 0 14px;list-style:none}
  .links li{font-size:11.5px;line-height:22.6px}
  .links li::before{content:"<<";color:var(--green);font-size:10px;margin-right:4px}

  .story-head{position:absolute;font-size:42px;line-height:44px;font-weight:300;text-transform:uppercase;letter-spacing:.5px}
  .story-head strong{font-weight:700}
  .deck{position:absolute;font-style:italic;font-size:16px}
  .body-copy{position:absolute;font-size:14px;line-height:23px;overflow:hidden}
  .body-copy p+p{margin-top:23px}
  .lead{color:var(--green);font-weight:700}

  .feature-photo{position:absolute;left:615px;top:144px;width:274px;height:303px;border:1.5px solid var(--frame);padding:7px}
  .feature-photo div{width:100%;height:100%;background:var(--photo)}
  .caption{position:absolute;left:615px;top:448px;font-style:italic;font-size:11.5px}
  .end-mark{display:inline-block;width:11px;height:11px;border-radius:50%;background:var(--blue);margin-left:5px;vertical-align:-1px}

  .column-rule{position:absolute;left:512px;top:629px;width:1px;height:522px;background:var(--rule)}
  .pull-quote{position:absolute;left:540px;top:926px;width:330px;padding:0 30px 0 44px;color:var(--blue);font-style:italic;font-weight:700;font-size:19px;line-height:26.5px}
  .pull-quote svg{position:absolute}

  .folio{position:absolute;right:22px;top:1172px;color:var(--green);font-weight:600;font-size:11.5px}
  .folio::after{content:"";display:inline-block;width:9px;height:18px;background:var(--green);margin-left:6px;vertical-align:-4px}
</style>
</head>
<body>
  <header class="masthead">
    <div class="brand">Harborline<br>Trade Group</div>
    <h1 class="title">NEWSLETTER</h1>
    <p class="tagline">Lorem ipsum dolor sit amet, consectetur adipisicing elit, sed do eiusmod tempor</p>
    <p class="issue">MAY 2014<br>ISSUE</p>
  </header>

  <aside>
    <h2 class="sidebar-head" style="top:145px">About Us</h2>
    <p class="sidebar-panel about">Lorem ipsum dolor sit amet, consectetur adipisicing elit, sed do eiusmod tempor incididunt ut labore et dolore magna aliqua. Ut enim ad minim veniam, quis nostrud exercitation ullamco laboris nisi ut aliquip ex ea commodo consequat.</p>
    <div class="sidebar-rule" style="top:474px"></div>

    <h2 class="sidebar-head" style="top:498px">In This Issue</h2>
    <ul class="sidebar-panel contents">
      <li>Lorem ipsum dolor<br>sit amet consectetur</li>
      <li>Lorem ipsum dolor<br>sit amet consectetur</li>
      <li>Lorem ipsum dolor<br>sit amet consectetur</li>
      <li>Lorem ipsum dolor<br>sit amet consectetur</li>
      <li>Lorem ipsum dolor<br>sit amet consectetur</li>
    </ul>
    <div class="sidebar-rule" style="top:897px"></div>

    <h2 class="sidebar-head" style="top:917px">Links</h2>
    <ul class="sidebar-panel links">
      <li>Lorem ipsum dolor sit amet</li>
      <li>Lorem ipsum dolor sit amet</li>
      <li>Lorem ipsum dolor sit amet</li>
      <li>Lorem ipsum dolor sit amet</li>
      <li>Lorem ipsum dolor sit amet</li>
      <li>Lorem ipsum dolor sit amet</li>
      <li>Lorem ipsum dolor sit amet</li>
      <li>Lorem ipsum dolor sit amet</li>
    </ul>
    <div class="sidebar-rule" style="top:1156px"></div>
  </aside>

  <article class="feature">
    <h2 class="story-head" style="left:271px;top:138px"><strong>Feature</strong> Story</h2>
    <p class="deck" style="left:271px;top:186px">Lorem ipsum dolor sit amet, consectetur</p>
    <div class="body-copy" style="left:271px;top:220px;width:325px;height:253px">
      <p><span class="lead">Lorem ipsum dolor</span> sit amet, consectetur adipisicing elit, sed do eiusmod tempor incididunt ut labore et dolore magna aliqua. Ut enim ad minim veniam, quis nostrud exercitation ullamco laboris nisi ut aliquip ex ea commodo consequat. Duis aute irure dolor in reprehenderit in voluptate velit esse cillum dolore eu fugiat nulla pariatur. Excepteur sint occaecat cupidatat non proident, sunt in culpa qui officia deserunt mollit anim id est laborum.</p>
    </div>
    <figure>
      <div class="feature-photo"><div role="img" aria-label="Feature story photograph"></div></div>
      <figcaption class="caption">Lorem ipsum dolor</figcaption>
    </figure>
    <div class="body-copy" style="left:271px;top:477px;width:620px;height:115px">
      <p>Lorem ipsum dolor sit amet, consectetur adipisicing elit, sed do eiusmod tempor incididunt ut labore et dolore magna aliqua. Ut enim ad minim veniam, quis nostrud exercitation ullamco laboris nisi ut aliquip ex ea commodo consequat. Duis aute irure dolor in reprehenderit in voluptate velit esse cillum dolore eu fugiat nulla pariatur. Excepteur sint occaecat cupidatat non proident, sunt in culpa qui officia deserunt mollit anim id est laborum.<span class="end-mark"></span></p>
    </div>
  </article>

  <article class="story-left">
    <h2 class="story-head" style="left:271px;top:622px"><strong>Other</strong><br>Story</h2>
    <p class="deck" style="left:271px;top:712px">Lorem ipsum dolor sit amet,</p>
    <div class="body-copy" style="left:271px;top:746px;width:220px;height:418px">
      <p><span class="lead">Lorem ipsum dolor</span> sit amet, consectetur adipisicing elit, sed do eiusmod tempor incididunt ut labore et dolore magna aliqua. Ut enim ad minim veniam, quis nostrud exercitation ullamco laboris nisi ut aliquip ex ea commodo consequat. Duis aute irure dolor in reprehenderit in voluptate velit esse cillum dolore eu fugiat nulla pariatur. Excepteur sint occaecat cupidatat non proident, sunt in culpa qui officia deserunt mollit anim id est laborum.</p>
      <p>Lorem ipsum dolor sit amet, consectetur adipisicing elit, sed do eiusmod tempor</p>
    </div>
  </article>

  <div class="column-rule"></div>

  <article class="story-right">
    <h2 class="story-head" style="left:536px;top:622px"><strong>Other</strong> Story</h2>
    <p class="deck" style="left:536px;top:664px">Lorem ipsum dolor sit amet, consectetur</p>
    <div class="body-copy" style="left:536px;top:697px;width:355px;height:230px">
      <p><span class="lead">Lorem ipsum dolor</span> sit amet, consectetur adipisicing elit, sed do eiusmod tempor incididunt ut labore et dolore magna aliqua. Ut enim ad minim veniam, quis nostrud exercitation ullamco laboris nisi ut aliquip ex ea commodo consequat. Duis aute irure dolor in reprehenderit in voluptate velit esse cillum dolore eu fugiat nulla pariatur. Excepteur sint occaecat cupidatat non proident, sunt in culpa qui officia deserunt mollit anim id est laborum.</p>
    </div>
    <blockquote class="pull-quote">
      <svg style="left:0;top:2px" width="30" height="26" viewBox="0 0 30 26" aria-hidden="true"><path d="M2 26V14L9 0h5L10 12h4v14zM17 26V14l7-14h5l-4 12h4v14z" fill="currentColor"/></svg>
      Lorem ipsum dolor sit amet, consectetur adipisicing elit, sed do eiusmod tempor incididunt ut labore et dolore magna aliqua.
      <svg style="left:188px;top:108px" width="30" height="26" viewBox="0 0 30 26" aria-hidden="true"><path d="M28 0v12l-7 14h-5l4-12h-4V0zM13 0v12L6 26H1l4-12H1V0z" fill="currentColor"/></svg>
    </blockquote>
    <div class="body-copy" style="left:536px;top:1060px;width:355px;height:96px">
      <p>Lorem ipsum dolor sit amet, consectetur adipisicing elit, sed do eiusmod tempor incididunt ut labore et dolore magna aliqua. Ut enim ad minim veniam, quis nostrud exercitation ullamco laboris</p>
    </div>
  </article>

  <footer class="folio">HTG MAY 2014</footer>
</body>
</html>
```